Email Newsletter Banner

I require 2 new email newsletter and web banners to be made up.
I require the brand names to be included on the banner which are " Wire Dispatcher" and "PC Flashz". I would also like some sort of imagery and also a "sign up here" button. Please see below examples:
https://dataskyreports.lornexhub.com/
https://datawisdomsky.lornexhub.com/
https://datastoryvault.lornexhub.com/

```html
<!DOCTYPE html>
<html lang="en">
<head>
<meta charset="utf-8">
<title>Wire Dispatcher and PC Flashz – Newsletter Banners</title>
<link rel="stylesheet" href="https://fonts.googleapis.com/css2?family=Exo+2:wght@700&family=Montserrat:wght@600;700;800&display=swap">
<style>
  :root {
    --sheet-center: #ffffff;
    --sheet-edge: #d6d6d6;
    --label-grey: #9c9c9c;
    --navy-deep: #0a1a4a;
    --navy-mid: #12307a;
    --navy-blue: #1a4fa8;
    --teal-glow: #1d7f7a;
    --violet-edge: #3a1e5e;
    --cyan: #22d3f5;
    --white: #ffffff;
    --button-fill: #1f5f73;
  }

  * { box-sizing: border-box; margin: 0; padding: 0; }

  html, body {
    width: 1200px;
    height: 792px;
    overflow: hidden;
  }

  body {
    position: relative;
    background: radial-gradient(ellipse at 50% 45%, var(--sheet-center) 35%, var(--sheet-edge) 100%);
    font-family: "Montserrat", Arial, sans-serif;
  }

  .size-label {
    position: absolute;
    left: 0;
    width: 1200px;
    text-align: center;
    font-weight: 600;
    font-size: 25px;
    letter-spacing: 0.5px;
    color: var(--label-grey);
  }

  .banner {
    position: absolute;
    height: 100px;
    overflow: hidden;
    display: flex;
    align-items: center;
  }
  .banner--wide { left: 62px; width: 1076px; }
  .banner--leader { left: 196px; width: 807px; }

  .banner-art {
    position: absolute;
    inset: 0;
  }
  .banner-art--circuit {
    background:
      radial-gradient(ellipse at 6% 100%, rgba(29,127,122,0.55) 0%, transparent 40%),
      radial-gradient(ellipse at 55% 20%, rgba(40,110,210,0.45) 0%, transparent 55%),
      linear-gradient(90deg, var(--navy-mid) 0%, var(--navy-blue) 45%, var(--navy-deep) 75%, var(--violet-edge) 100%);
  }
  .banner-art--pixel {
    background:
      radial-gradient(ellipse at 20% 0%, rgba(34,211,245,0.35) 0%, transparent 30%),
      radial-gradient(ellipse at 55% 100%, rgba(34,150,245,0.35) 0%, transparent 30%),
      radial-gradient(ellipse at 80% 40%, rgba(40,90,190,0.45) 0%, transparent 45%),
      linear-gradient(90deg, var(--navy-deep) 0%, var(--navy-mid) 50%, var(--navy-deep) 100%);
  }

  .brand {
    position: relative;
    display: flex;
    align-items: center;
    gap: 14px;
  }
  .brand-mark {
    flex: none;
    background: var(--cyan);
  }
  .brand-mark--circle { width: 40px; height: 40px; border-radius: 50%; }
  .brand-mark--square { width: 44px; height: 44px; background: var(--white); }

  .brand-name {
    font-family: "Exo 2", "Trebuchet MS", sans-serif;
    font-weight: 700;
    font-size: 44px;
    line-height: 1;
    letter-spacing: 0.5px;
    text-transform: uppercase;
    color: var(--cyan);
    white-space: nowrap;
  }
  .brand-name--light { color: var(--white); }

  .tagline {
    position: relative;
    font-weight: 700;
    font-size: 12.5px;
    line-height: 1.2;
    color: var(--white);
    text-transform: uppercase;
    white-space: nowrap;
  }

  .signup-button {
    position: absolute;
    right: 0;
    top: 35px;
    height: 34px;
    padding: 0 18px 0 16px;
    display: flex;
    align-items: center;
    background: var(--button-fill);
    border: 2px solid var(--white);
    border-right: none;
    border-radius: 17px 0 0 17px;
    font-weight: 800;
    font-size: 14px;
    color: var(--white);
    text-transform: uppercase;
    white-space: nowrap;
  }
</style>
</head>
<body>

  <div class="size-label" style="top:36px;">970X90</div>
  <section class="banner banner--wide" style="top:83px;">
    <div class="banner-art banner-art--circuit" role="img" aria-label="Glowing blue circuit board line art background"></div>
    <div class="brand" style="margin-left:28px;">
      <span class="brand-mark brand-mark--circle"></span>
      <span class="brand-name">Wire Dispatcher</span>
    </div>
    <p class="tagline" style="margin-left:40px;">Essential whitepapers<br>for IT professionals</p>
    <span class="signup-button">Sign up here</span>
  </section>

  <div class="size-label" style="top:210px;">728X90</div>
  <section class="banner banner--leader" style="top:260px;">
    <div class="banner-art banner-art--circuit" role="img" aria-label="Glowing blue circuit board line art background"></div>
    <div class="brand" style="margin-left:16px;">
      <span class="brand-mark brand-mark--circle"></span>
      <span class="brand-name" style="font-size:38px;">Wire Dispatcher</span>
    </div>
    <p class="tagline" style="margin-left:20px; font-size:11.5px;">Delivering the latest IT<br>news to your inbox</p>
    <span class="signup-button" style="font-size:13px; padding:0 12px;">Sign up here</span>
  </section>

  <div class="size-label" style="top:404px;">970X90</div>
  <section class="banner banner--wide" style="top:447px;">
    <div class="banner-art banner-art--pixel" role="img" aria-label="Dark blue technology schematic background with scattered pixel blocks"></div>
    <div class="brand" style="margin-left:38px;">
      <span class="brand-mark brand-mark--square"></span>
      <span class="brand-name">PC Flashz</span>
    </div>
    <p class="tagline" style="margin-left:18px;">Delivering the latest IT<br>news to your inbox</p>
    <span class="signup-button">Sign up here</span>
  </section>

  <div class="size-label" style="top:580px;">728X90</div>
  <section class="banner banner--leader" style="top:623px;">
    <div class="banner-art banner-art--pixel" role="img" aria-label="Dark blue technology schematic background with scattered pixel blocks"></div>
    <div class="brand" style="margin-left:18px;">
      <span class="brand-mark brand-mark--square"></span>
      <span class="brand-name">PC Flashz</span>
    </div>
    <p class="tagline" style="margin-left:18px;">Delivering the latest IT<br>news to your inbox</p>
    <span class="signup-button" style="font-size:13px; padding:0 12px;">Sign up here</span>
  </section>

</body>
</html>
```